BRINDLEWAVE is a New Zealand based aerial imaging company performing mapping, surveying and videography

I would like a business card that is contemporary and clean. The font for the business name is called Gtec Technology and I would like to have the text "AERIAL IMAGING" under the "BRINDLEWAVE" name in a font similar to URW Gothic or another light modern font. Brindlewave performs aerial imaging projects using a hexacopter UAV. Surveying and mapping with 3D Digital Elevation Models are a focus, I also produce aerial photographs and video's including post editing.
Updates

Target Market(s)

Industrial plant managers, Property owners, Event organisers.

Industry/Entity Type

Videography

Contact Information for Business Card

BRINDLEWAVE AERIAL IMAGING. Owner Ross Pellow. Cell: 027 4913068. P.O. Box 8321 Dunedin, New Zealand.

Font styles to use
Other font styles liked:
• Gtec Technology

Colors
9bcb3b
33a6d7
ec1f27

Requirements
Must have
• Modern professional look.
Nice to have
• Perhaps an aerial image of a landscape who's location is not identifiable. Maybe use included image of my hexacopter on the back of the card? Not compulsory though.
Should not have
• Clip Art style images.

```html
<!DOCTYPE html>
<html lang="en">
<head>
<meta charset="utf-8">
<title>Brindlewave Aerial Imaging — Business Card</title>
<link rel="stylesheet" href="https://fonts.googleapis.com/css2?family=Jost:wght@300;400;500;600;700&display=swap">
<style>
  :root {
    --ink: #000000;
    --paper: #ffffff;
    --leaf: #8dc63f;
    --mist: #9a9c9e;
    --sky-top: #c9d3e2;
    --sky-mid: #dfe4ea;
    --hills: #8b9aa6;
    --meadow: #5f8a3a;
    --label: #111111;
  }
  * { margin: 0; padding: 0; box-sizing: border-box; }
  html, body { width: 1200px; height: 476px; overflow: hidden; background: var(--paper); }
  body { position: relative; font-family: "Jost", sans-serif; color: var(--ink); }

  .card { position: absolute; top: 59px; width: 548px; height: 343px; overflow: hidden; background: var(--paper); }
  .card--front { left: 38px; }
  .card--back { left: 620px; }

  .card__band { position: absolute; left: 0; bottom: 0; width: 100%; height: 16px; background: var(--leaf); }

  /* front */
  .front__arc { position: absolute; inset: 0; width: 100%; height: 100%; }
  .brand { position: absolute; top: 48px; left: 0; width: 100%; text-align: center; color: var(--paper); }
  .brand__name { font-size: 40px; font-weight: 600; letter-spacing: 0.06em; line-height: 1; }
  .brand__tagline { margin-top: 8px; font-size: 20px; font-weight: 300; letter-spacing: 0.32em; line-height: 1; padding-left: 0.32em; }

  .contact { position: absolute; left: 0; width: 100%; text-align: center; line-height: 1; }
  .contact__name { top: 176px; font-size: 21px; font-weight: 700; }
  .contact__role { top: 201px; font-size: 11px; font-weight: 400; }
  .contact__cell { top: 215px; font-size: 17px; font-weight: 400; letter-spacing: 0.03em; }
  .contact__company { top: 278px; font-size: 14px; font-weight: 400; }
  .contact__address { top: 298px; font-size: 17px; font-weight: 400; }

  /* back */
  .back__photo {
    position: absolute; inset: 0 0 16px 0;
    background:
      linear-gradient(90deg, var(--paper) 0%, rgba(255,255,255,0.85) 18%, rgba(255,255,255,0) 45%),
      linear-gradient(180deg, var(--sky-top) 0%, var(--sky-mid) 45%, var(--hills) 65%, var(--meadow) 85%, #4f7a34 100%);
  }
  .services { position: absolute; top: 10px; left: 12px; line-height: 1; white-space: nowrap; font-weight: 400; }
  .services__line { display: block; }
  .tone-leaf { color: var(--leaf); }
  .tone-mist { color: var(--mist); }
  .services__line--one { font-size: 30px; }
  .services__line--one .small { font-size: 17px; }
  .services__line--two { margin-top: 2px; font-size: 18px; letter-spacing: 0.02em; }
  .services__line--three { margin-top: 4px; font-size: 23px; }
  .services__line--three .large { font-size: 28px; }
  .services__line--three .small { font-size: 16px; }
  .services__line--four { margin-top: 2px; font-size: 22px; }
  .services__line--five { margin-top: 4px; font-size: 20px; }
  .services__line--five .small { font-size: 15px; }
  .services__line--six { margin-top: 9px; font-size: 13px; }
  .services__line--seven { margin-top: 7px; font-size: 13px; }

  .caption { position: absolute; top: 428px; font-size: 21px; font-weight: 600; letter-spacing: 0.06em; color: var(--label); }
  .caption--front { left: 56px; }
  .caption--back { left: 655px; }
</style>
</head>
<body>

<section class="card card--front" aria-label="Front of business card">
  <svg class="front__arc" viewBox="0 0 548 343" preserveAspectRatio="none" aria-hidden="true">
    <path d="M0 0 H548 V199 Q274 100 0 199 Z" fill="var(--ink)"/>
  </svg>
  <div class="brand">
    <div class="brand__name">BRINDLEWAVE</div>
    <div class="brand__tagline">Aerial Imaging</div>
  </div>
  <div class="contact contact__name">Ross Pellow</div>
  <div class="contact contact__role">Owner</div>
  <div class="contact contact__cell">Cell: 027 4913068</div>
  <div class="contact contact__company">BRINDLEWAVE AERIAL IMAGING</div>
  <div class="contact contact__address">P.O. Box 8321 Dunedin, New Zealand.</div>
  <div class="card__band"></div>
</section>

<section class="card card--back" aria-label="Back of business card">
  <div class="back__photo" role="img" aria-label="Photo of a hexacopter drone hovering over a lake with misty mountains, trees and lavender fields"></div>
  <div class="services">
    <span class="services__line services__line--one"><span class="tone-leaf small">Brindlewave</span> <span class="tone-leaf">aerial imaging</span></span>
    <span class="services__line services__line--two tone-mist">hexacopter UAV Surveying &amp; mapping</span>
    <span class="services__line services__line--three tone-leaf"><span class="large">3D</span> Digital Elevation <span class="small">Models</span></span>
    <span class="services__line services__line--four tone-mist">aerial photograph</span>
    <span class="services__line services__line--five tone-leaf">video <span class="small">post editing</span></span>
    <span class="services__line services__line--six tone-mist">UAV Surveying &amp; mapping</span>
    <span class="services__line services__line--seven tone-leaf">Brindlewave aerial imaging</span>
  </div>
  <div class="card__band"></div>
</section>

<div class="caption caption--front">FRONT CARD DESIGN</div>
<div class="caption caption--back">BACK CARD DESIGN</div>

</body>
</html>
```